Morrow & Pellant Stationery

Greetings again. Now we've got an awesome logo, it's time to get the stationery to go with it. We require the following items of stationery:

- Business Card - Print Ready, all we need to do is change names and numbers and submit to printer.  Double sided with logo on one side and details on the other side. (85mm x 55mm)

- With Compliments Slip

- Letterhead - These will be preprinted pages that will then be used as pages.
(A4)

- Envelope - Business Size(Standard DL)

Target Market(s)

Essentially, this firm services clients facing criminal charges and/or seeking legal aid. The firm is also looking at taking on more white-collar crime cases.

Requirements
Must have
• - Same Design Cues & Colours as the Branding details attached

• - Address (as follows)

• Suite 8

• 212-216 Carrow St

• DANDENONG VIC 3175

• Phone: (03) 9555 0142

• Fax: (03) 9555 0187

• Web: www.morrowandpellant.example

• - Colour: Pantone 194 (Red)

```html
<!DOCTYPE html>
<html lang="en">
<head>
<meta charset="utf-8">
<title>Morrow &amp; Pellant Stationery</title>
<link rel="stylesheet" href="https://fonts.googleapis.com/css2?family=Cinzel:wght@600&family=EB+Garamond:wght@400;600&family=Pinyon+Script&display=swap">
<style>
  :root {
    --brand: #a6093d;
    --ink: #111111;
    --soft-ink: #3a3a3a;
    --rule: #b5b5b5;
    --outline: #111111;
    --paper: #ffffff;
  }
  * { box-sizing: border-box; margin: 0; padding: 0; }
  html, body { width: 1200px; height: 1123px; overflow: hidden; background: var(--paper); }
  .sheet { position: relative; width: 1200px; height: 1123px; font-family: "EB Garamond", Georgia, serif; color: var(--ink); }

  .piece { position: absolute; background: var(--paper); border: 1.5px solid var(--outline); }
  .card-front  { left: 2px;   top: 4px;   width: 494px; height: 287px; border-radius: 6px 22px 22px 20px; }
  .card-back   { left: 1px;   top: 308px; width: 494px; height: 287px; border-radius: 6px 22px 22px 20px; }
  .comp-slip   { left: 68px;  top: 621px; width: 373px; height: 248px; border-radius: 10px; border-width: 2px; }
  .letterhead  { left: 534px; top: 1px;   width: 662px; height: 856px; border-radius: 30px; border-width: 2px; }
  .envelope-front { left: 4px;   top: 903px; width: 516px; height: 218px; border-width: 2px; }
  .envelope-back  { left: 681px; top: 903px; width: 516px; height: 218px; border-width: 2px; }
  .envelope-flap {
    position: absolute; left: -2px; top: -2px; width: 516px; height: 88px;
    border: 2px solid var(--outline); border-radius: 0 0 12px 12px;
  }

  .brand-dot { position: absolute; border-radius: 50%; background: var(--brand); }

  .lockup { position: absolute; white-space: nowrap; }
  .lockup-name { font-family: "Cinzel", "Times New Roman", serif; font-weight: 600; color: var(--ink); line-height: 1; display: block; }
  .lockup-tagline { font-family: "Cinzel", "Times New Roman", serif; font-weight: 600; color: var(--ink); line-height: 1; display: block; letter-spacing: 0.12em; }

  .centered { position: absolute; left: 0; width: 100%; text-align: center; }
  .holder-name { font-weight: 600; color: var(--brand); font-size: 21px; letter-spacing: 0.02em; }
  .holder-role { font-size: 19px; }
  .card-divider { position: absolute; left: 80px; top: 496px; width: 321px; height: 1.5px; background: var(--rule); }
  .contact { line-height: 1.25; }
  .card-back .contact { font-size: 17px; top: 203px; }
  .comp-line { font-family: "Pinyon Script", cursive; font-size: 24px; color: var(--ink); }
  .comp-slip .contact { font-size: 7px; top: 219px; color: var(--soft-ink); line-height: 1.15; }
  .letterhead .contact { font-size: 13px; top: 767px; color: var(--soft-ink); line-height: 0.95; }
</style>
</head>
<body>
<main class="sheet">

  <section class="piece card-front" aria-label="Business card, front">
    <span class="brand-dot" style="left:59px; top:92px; width:94px; height:94px;"></span>
    <div class="lockup" style="left:189px; top:121px;">
      <span class="lockup-name" style="font-size:27px;">Morrow &amp; Pellant</span>
      <span class="lockup-tagline" style="font-size:14px; margin-top:4px;">Barristers &amp; Solicitors</span>
    </div>
  </section>

  <section class="piece card-back" aria-label="Business card, back">
    <span class="brand-dot" style="left:200px; top:14px; width:83px; height:83px;"></span>
    <p class="centered holder-name" style="top:120px;">HOLDERS NAME</p>
    <p class="centered holder-role" style="top:145px;">Holders Position</p>
    <div class="card-divider" style="top:188px;"></div>
    <p class="centered contact">Suite 8 - 212-216 Carrow St&nbsp; Dandenong VIC 3175<br>Phone: (03) 9555 0142&nbsp; Fax: (03) 9555 0187<br>www.morrowandpellant.example</p>
  </section>

  <section class="piece comp-slip" aria-label="With compliments slip">
    <span class="brand-dot" style="left:133px; top:25px; width:27px; height:27px;"></span>
    <div class="lockup" style="left:169px; top:32px;">
      <span class="lockup-name" style="font-size:8.5px;">Morrow &amp; Pellant</span>
      <span class="lockup-tagline" style="font-size:4.5px; margin-top:1px;">Barristers &amp; Solicitors</span>
    </div>
    <p class="centered comp-line" style="top:62px;">With compliments</p>
    <p class="centered contact">Suite 8 - 212-216 Carrow St&nbsp; Dandenong VIC 3175<br>Phone: (03) 9555 0142&nbsp; Fax: (03) 9555 0187<br>www.morrowandpellant.example</p>
  </section>

  <section class="piece letterhead" aria-label="Letterhead">
    <span class="brand-dot" style="left:192px; top:66px; width:70px; height:70px;"></span>
    <div class="lockup" style="left:287px; top:88px;">
      <span class="lockup-name" style="font-size:20px;">Morrow &amp; Pellant</span>
      <span class="lockup-tagline" style="font-size:10.5px; margin-top:3px;">Barristers &amp; Solicitors</span>
    </div>
    <p class="centered contact">Suite 8 - 212-216 Carrow St&nbsp; Dandenong VIC 3175<br>Phone: (03) 9555 0142&nbsp; Fax: (03) 9555 0187<br>www.morrowandpellant.example</p>
  </section>

  <section class="piece envelope-front" aria-label="DL envelope, front">
    <span class="brand-dot" style="left:10px; top:11px; width:37px; height:37px;"></span>
    <div class="lockup" style="left:59px; top:21px;">
      <span class="lockup-name" style="font-size:12px;">Morrow &amp; Pellant</span>
      <span class="lockup-tagline" style="font-size:6px; margin-top:2px;">Barristers &amp; Solicitors</span>
    </div>
  </section>

  <section class="piece envelope-back" aria-label="DL envelope, back">
    <div class="envelope-flap"></div>
    <span class="brand-dot" style="left:224px; top:15px; width:56px; height:56px;"></span>
  </section>

</main>
</body>
</html>
```